Business Card Design Project

Attached is a rough business card design. We like this general design but we feel that the layout, text, color can use improvement and we seek the help of a professional designer.
We have a television and film production company based in New York. We need our cards for television network executives, other production executives, financiers etc. We deal with creative types as well as business people so we need the card to be interesting and edgy just like the name of our company - KICKTHECAN. The design should reflect the edgy, punk rock attitude of our company.
We prefer orange typeface for the logo but we're open to other ideas. I am attaching our existing business card and other files to help with the design.
Thank you in advance!!
Updates
Target Market(s)
Television and film producers, television network executives, other production executives, financiers, distribution companies
Industry/Entity Type
Film Production
Requirements
Must have
- I am attaching a photo of the company mascot which is a dog. We prefer to have the dog's photo as part of the card but we're open to the other ideas.
Name, phone number, email

```html
<!DOCTYPE html>
<html lang="en">
<head>
<meta charset="utf-8">
<title>Kick The Can Productions – Business Card</title>
<link rel="stylesheet" href="https://fonts.googleapis.com/css2?family=Open+Sans:ital,wght@0,400;0,700;1,400&display=swap">
<style>
  :root {
    --backdrop: #ecebe8;
    --band-dark: #3c3c3f;
    --bar-dark: #1e1d22;
    --brand-orange: #f0913f;
    --peach: #f2b999;
    --peach-light: #f6c7ab;
    --ink: #1f1a18;
    --white: #ffffff;
    --photo-warm: #d9a27e;
    --photo-deep: #a9704f;
    --photo-shadow: #6e4a38;
  }
  * { margin: 0; padding: 0; box-sizing: border-box; }
  html, body {
    width: 1200px; height: 1000px; overflow: hidden;
    background: var(--backdrop);
  }
  .canvas {
    width: 1200px; height: 1000px;
    display: flex; align-items: center; justify-content: center;
  }
  .card {
    position: relative;
    width: 500px; height: 860px;
    border-radius: 44px;
    overflow: hidden;
    background: var(--peach);
    box-shadow: 0 14px 36px rgba(0,0,0,0.18);
    font-family: "Open Sans", Arial, sans-serif;
    color: var(--ink);
  }
  .brand-band {
    height: 108px;
    background: var(--band-dark);
    display: flex; align-items: center; justify-content: center;
    gap: 16px;
  }
  .brand-dot {
    width: 18px; height: 18px;
    border-radius: 50%;
    background: var(--brand-orange);
  }
  .brand-name {
    font-family: "Open Sans", Arial, sans-serif;
    font-weight: 700;
    font-size: 38px;
    letter-spacing: 2px;
    text-transform: uppercase;
    color: var(--brand-orange);
  }
  .mascot-photo {
    height: 430px;
    background: radial-gradient(ellipse at 45% 45%, var(--photo-warm) 0%, var(--photo-deep) 60%, var(--photo-shadow) 100%);
    position: relative;
  }
  .mascot-photo::after {
    content: "";
    position: absolute; left: 0; right: 0; bottom: 0; height: 140px;
    background: linear-gradient(to bottom, rgba(242,185,153,0), var(--peach));
  }
  .person {
    padding: 22px 40px 0 0;
    text-align: right;
  }
  .person-name {
    font-size: 40px; font-weight: 400; line-height: 1.1;
  }
  .person-email {
    font-size: 21px; margin-top: 4px;
  }
  .web-bar {
    margin-top: 30px;
    height: 56px;
    background: var(--bar-dark);
    display: flex; align-items: center; justify-content: center;
    border-top: 2px solid var(--peach-light);
  }
  .web-address {
    color: var(--white);
    font-weight: 700;
    font-size: 28px;
  }
  .company-details {
    text-align: center;
    font-size: 16px;
    line-height: 1.45;
    margin-top: 14px;
    text-transform: uppercase;
  }
  .company-name { font-style: italic; }
  .company-email { text-transform: none; }
</style>
</head>
<body>
<main class="canvas">
  <article class="card">
    <header class="brand-band">
      <span class="brand-dot"></span>
      <span class="brand-name">Kick The Can</span>
    </header>
    <div class="mascot-photo" role="img" aria-label="Photo of the company mascot dog lying down with a small soccer ball"></div>
    <section class="person">
      <p class="person-name">Marcus Delgado</p>
      <p class="person-email">marcus@kickthecan.com</p>
    </section>
    <div class="web-bar">
      <span class="web-address">www.kickthecan.com</span>
    </div>
    <section class="company-details">
      <p class="company-name">Kick The Can Productions</p>
      <p>145 West 48th Street, #9C, New York, NY 10036</p>
      <p>Phone: (917) 555-0182</p>
      <p>Email: <span class="company-email">info@kickthecan.com</span></p>
    </section>
  </article>
</main>
</body>
</html>
```